Bref créative
BRN Tek
B-cards, letter head and envelopes
I need single sided standard sized Business Card [3.5" x 2"]
use same font or others...other fonts are welcome
Simple
Gareth Pembly
CEO
482 Harlowe Street, Suite 1730
San Francisco, California 94111
gpembly@brnqel.com
brnqel.com
-use this logo in the business cards, letterhead and envelopes.
-we are looking for designs with and with out a water mark using parts or the entire logo.

```html
<!DOCTYPE html>
<html lang="en">
<head>
<meta charset="utf-8">
<title>BRN Tek Stationery</title>
<link rel="stylesheet" href="https://fonts.googleapis.com/css2?family=Open+Sans:wght@400;600;700&display=swap">
<style>
  :root {
    --navy: #3d5e88;
    --navy-dark: #34527a;
    --green: #7bb843;
    --grey-text: #7d8590;
    --paper: #ffffff;
    --edge: #d6d9de;
    --faint: #eceef2;
    --bg: #ffffff;
  }
  * { box-sizing: border-box; margin: 0; padding: 0; }
  html, body { width: 1200px; height: 737px; overflow: hidden; background: var(--bg); }
  body { position: relative; font-family: "Open Sans", Arial, sans-serif; color: var(--grey-text); }

  .sheet { position: absolute; background: var(--paper); border: 1px solid var(--edge); overflow: hidden; }

  .brand { position: absolute; display: flex; flex-direction: column; }
  .brand-name { font-weight: 700; color: var(--green); line-height: 1; letter-spacing: 1px; }
  .brand-tagline { font-size: 5px; color: var(--grey-text); margin-top: 3px; letter-spacing: .3px; }

  .watermark { position: absolute; font-weight: 700; color: var(--faint); line-height: 1; letter-spacing: 6px; }

  /* Letterhead */
  .letterhead { left: 29px; top: 34px; width: 528px; height: 643px; }
  .letterhead .brand { left: 20px; top: 12px; }
  .letterhead .brand-name { font-size: 44px; }
  .letterhead .watermark { right: -10px; bottom: 70px; font-size: 160px; }
  .letterhead-footer { position: absolute; left: 0; right: 0; bottom: 0; height: 50px; }
  .letterhead-footer .rule { height: 3px; background: var(--green); }
  .letterhead-footer .band { height: 47px; background: var(--navy); }
  .letterhead-address { position: absolute; left: 0; right: 0; bottom: 54px; text-align: center; font-size: 7.5px; line-height: 1.5; color: var(--navy); }

  /* Envelope front */
  .envelope-front { left: 581px; top: 29px; width: 595px; height: 253px; }
  .envelope-front .brand { left: 18px; top: 10px; }
  .envelope-front .brand-name { font-size: 40px; }
  .envelope-front .watermark { right: 20px; top: 40px; font-size: 120px; }
  .envelope-band { position: absolute; left: 0; right: 0; bottom: 0; height: 54px; }
  .envelope-band .rule { height: 3px; background: var(--green); }
  .envelope-band .band { height: 51px; background: var(--navy); padding: 10px 10px 0; font-size: 8px; color: #dfe6ef; }

  /* Envelope back */
  .envelope-back { left: 581px; top: 318px; width: 595px; height: 206px; background: var(--navy); border-color: var(--navy); }
  .envelope-flap { position: absolute; left: 0; top: 0; right: 0; height: 30px; background: var(--navy-dark); }
  .envelope-back .brand { left: 50%; top: 72px; transform: translateX(-50%); align-items: center; }
  .envelope-back .brand-name { font-size: 46px; color: #ffffff; }
  .envelope-back .site { position: absolute; left: 0; right: 0; top: 56px; text-align: center; font-size: 5px; color: #dfe6ef; }

  /* Business cards */
  .card { width: 226px; height: 136px; top: 574px; }
  .card-front { left: 566px; }
  .card-front .contact { position: absolute; left: 8px; top: 8px; font-size: 4.5px; line-height: 1.55; color: var(--grey-text); }
  .card-front .contact .person { font-size: 8px; font-weight: 700; color: var(--navy); line-height: 1.2; }
  .card-front .contact .role { font-size: 5px; margin-bottom: 6px; }
  .card-front .brand { left: 122px; top: 36px; }
  .card-front .brand-name { font-size: 36px; }
  .card-front .card-strip { position: absolute; left: 0; right: 0; bottom: 0; height: 18px; border-top: 2px solid var(--green); background: var(--navy); }

  .card-back { left: 845px; background: var(--navy); border-color: var(--navy); }
  .card-back .brand { left: 60px; top: 38px; }
  .card-back .brand-name { font-size: 38px; color: #ffffff; }
  .card-back .brand-tagline { color: #dfe6ef; }
</style>
</head>
<body>

<section class="sheet letterhead">
  <div class="brand"><span class="brand-name">BRN</span><span class="brand-tagline">Business Resource Network</span></div>
  <div class="watermark" aria-hidden="true">BRN</div>
  <p class="letterhead-address">482 Harlowe Street, Suite 1730, San Francisco, California 94111<br>Toll free: 800-555-0147 | Phone: 415-555-0182 | Fax: 415-555-0193 | brnqel.com</p>
  <div class="letterhead-footer"><div class="rule"></div><div class="band"></div></div>
</section>

<section class="sheet envelope-front">
  <div class="brand"><span class="brand-name">BRN</span><span class="brand-tagline">Business Resource Network</span></div>
  <div class="watermark" aria-hidden="true">BRN</div>
  <div class="envelope-band"><div class="rule"></div><div class="band">482 Harlowe Street, Suite 1730, San Francisco, California 94111</div></div>
</section>

<section class="sheet envelope-back">
  <div class="envelope-flap"></div>
  <p class="site">brnqel.com</p>
  <div class="brand"><span class="brand-name">BRN</span></div>
</section>

<section class="sheet card card-front">
  <div class="contact">
    <div class="person">Gareth Pembly</div>
    <div class="role">CEO</div>
    482 Harlowe Street, Suite 1730<br>
    San Francisco, California 94111<br>
    Phone: 415-555-0182<br>
    Fax: 415-555-0193<br>
    gpembly@brnqel.com<br>
    brnqel.com
  </div>
  <div class="brand"><span class="brand-name">BRN</span><span class="brand-tagline">Business Resource Network</span></div>
  <div class="card-strip"></div>
</section>

<section class="sheet card card-back">
  <div class="brand"><span class="brand-name">BRN</span><span class="brand-tagline">Business Resource Network</span></div>
</section>

</body>
</html>
```